Luminously Grounded Vitality

We want to design a business card that is modern and appealing for an innovative psychedelic telemedicine company that provides at-home ketamine-assisted therapy along with wellness, longevity, and anti-aging medicines. We want to use our deep purple and white plus other colors you can find on our website. We don't have any strict brand guidelines yet so feel free to get creative. We want a very professional, but technology first modern design that will instill trust, peace, calm, but also be attractive to investors in the healthcare and SaaS space.

```html
<!DOCTYPE html>
<html lang="en">
<head>
<meta charset="UTF-8">
<title>Luminously Grounded Vitality — Business Card</title>
<link rel="stylesheet" href="https://fonts.googleapis.com/css2?family=Nunito:wght@400;600;700;800&display=swap">
<style>
  :root {
    --bg: #e4e4e6;
    --paper: #f3f3f2;
    --ink: #2b2838;
    --violet: #6b4fa3;
    --mauve: #8a5b96;
    --purple-light: #9150e6;
    --purple-deep: #6a34c2;
    --white: #ffffff;
  }
  * { box-sizing: border-box; margin: 0; padding: 0; }
  html, body { width: 1200px; height: 800px; overflow: hidden; }
  body {
    background: var(--bg);
    font-family: "Nunito", sans-serif;
    color: var(--ink);
    position: relative;
  }
  .card {
    position: absolute;
    top: 242px;
    width: 520px;
    height: 316px;
    box-shadow: 0 6px 18px rgba(0,0,0,0.12);
  }
  /* Front */
  .card-front {
    left: 70px;
    background: var(--paper);
    display: flex;
    align-items: center;
  }
  .brand {
    width: 220px;
    display: flex;
    flex-direction: column;
    align-items: center;
    text-align: center;
    padding-left: 18px;
  }
  .brand-dot {
    width: 34px; height: 34px;
    border-radius: 50%;
    background: var(--violet);
    margin-bottom: 14px;
  }
  .brand-name {
    font-size: 21px;
    font-weight: 600;
    line-height: 1.2;
    color: var(--mauve);
  }
  .contact { padding-left: 28px; }
  .person-name {
    font-size: 20px;
    font-weight: 700;
    color: var(--violet);
    letter-spacing: 0.2px;
  }
  .person-role {
    font-size: 15px;
    margin-top: 6px;
  }
  .rule {
    width: 42px; height: 2px;
    background: var(--violet);
    margin: 12px 0 30px;
  }
  .line {
    display: flex; align-items: center;
    font-size: 15px;
    line-height: 23px;
  }
  .line svg { width: 15px; height: 15px; margin-right: 9px; flex: none; }
  .address { font-size: 14.5px; line-height: 22px; margin-top: 10px; }
  .web { font-size: 15px; margin-top: 10px; }
  .web strong { font-weight: 700; }
  /* Back */
  .card-back {
    left: 610px;
    background: radial-gradient(ellipse at 60% 40%, var(--purple-light) 0%, var(--purple-deep) 80%);
    color: var(--white);
    display: flex;
    flex-direction: column;
    align-items: center;
    justify-content: center;
    text-align: center;
  }
  .back-name { font-size: 30px; font-weight: 600; line-height: 1.15; }
  .back-web { font-size: 15px; margin-top: 10px; letter-spacing: 0.4px; }
</style>
</head>
<body>
  <section class="card card-front">
    <div class="brand">
      <div class="brand-dot"></div>
      <div class="brand-name">Luminously Grounded Vitality</div>
    </div>
    <div class="contact">
      <div class="person-name">MARISOL VANTRELL</div>
      <div class="person-role">Manager</div>
      <div class="rule"></div>
      <div class="line">
        <svg viewBox="0 0 16 16" fill="none" stroke="#6b4fa3" stroke-width="1.3"><path d="M3 2h3l1.2 3-1.7 1.2a8 8 0 0 0 4.3 4.3L11 8.8l3 1.2v3a1 1 0 0 1-1 1A12 12 0 0 1 2 3a1 1 0 0 1 1-1z"/></svg>
        +1 833-555-0142
      </div>
      <div class="line">
        <svg viewBox="0 0 16 16" fill="none" stroke="#6b4fa3" stroke-width="1.3"><rect x="1.5" y="3.5" width="13" height="9" rx="1"/><path d="M2 4l6 5 6-5"/></svg>
        hello@luminouslygrounded.com
      </div>
      <div class="address">240 Aspen Lane, Suite 900, Boulder,<br>CO, United States, Colorado</div>
      <div class="web">www.<strong>luminouslygrounded</strong>.com</div>
    </div>
  </section>

  <section class="card card-back">
    <div class="back-name">Luminously Grounded<br>Vitality</div>
    <div class="back-web">www.luminouslygrounded.com</div>
  </section>
</body>
</html>
```